Real Estate Development, Finance and Fund Management company

We need a business card and logo design for a new company based in Asia called 'Qelmora Holdings Ltd.'
We provide full service large scale real estate development services, including fund management, project delivery services and acquisitions. We are looking for a bold logo with a strong feeling of security. A good reference would be the Marlowgate (www.marlowgate-example.com) or Tesmere Equity (www.tesmereeq-example.com).
We will need to have the imagery for the cards and logos to be produced for a dark and light background, and for web and print quality.
Initial thoughts are to have silver text on a black or dark grey background but leave that to your discretion.
Final design should communicate stability, financial safety and building on a solid foundation.
NOTE : We are not looking for pictures or clip art. Logo should be primarily from text and anything additional should be limited and tasteful.
Thanks!

```html
<!DOCTYPE html>
<html lang="en">
<head>
<meta charset="utf-8">
<title>Qelmora Holdings Ltd. – Business Card</title>
<link href="https://fonts.googleapis.com/css2?family=Questrial&family=Mulish:wght@700&display=swap" rel="stylesheet">
<style>
  :root {
    --page: #ffffff;
    --card-light: #2a2c31;
    --card-mid: #17181b;
    --card-dark: #0b0c0e;
    --silver: #c4c6c9;
    --silver-soft: #a6a9ad;
    --silver-dim: #8d9094;
    --edge: rgba(255,255,255,0.08);
  }
  * { margin: 0; padding: 0; box-sizing: border-box; }
  html, body {
    width: 1026px; height: 1200px; overflow: hidden;
    background: var(--page);
  }
  .sheet { position: relative; width: 1026px; height: 1200px; }

  .card {
    position: absolute;
    left: 51px; width: 927px; height: 502px;
    border-radius: 22px;
    background:
      radial-gradient(ellipse 70% 80% at 22% 18%, var(--card-light) 0%, var(--card-mid) 55%, var(--card-dark) 100%);
    box-shadow: 0 4px 10px rgba(0,0,0,0.35), inset 0 1px 0 var(--edge);
    font-family: "Questrial", "Century Gothic", sans-serif;
    color: var(--silver);
  }
  .card--front { top: 48px; }
  .card--back  { top: 650px; height: 498px; }

  .brand {
    position: absolute;
    white-space: nowrap;
    font-weight: 400;
    color: var(--silver);
    letter-spacing: -0.5px;
  }
  .card--front .brand { left: 0; right: 0; top: 52px; text-align: center; font-size: 64px; }
  .card--back  .brand { left: 0; right: 0; top: 168px; text-align: center; font-size: 62px; }

  .holder { position: absolute; left: 100px; top: 282px; width: 260px; text-align: center; }
  .holder__name {
    font-family: "Mulish", "Arial", sans-serif; font-weight: 700;
    font-size: 46px; color: var(--silver-soft); line-height: 1;
  }
  .holder__role { margin-top: 16px; font-size: 27px; color: var(--silver-dim); }

  .contact { position: absolute; right: 51px; top: 210px; list-style: none; }
  .contact__item {
    display: flex; align-items: center; justify-content: flex-end;
    font-size: 27px; line-height: 41px; color: var(--silver);
  }
  .contact__item--continued { padding-right: 46px; }
  .contact__icon { width: 26px; height: 26px; margin-left: 20px; fill: var(--silver); flex: none; }

  .website {
    position: absolute; right: 195px; top: 242px;
    font-size: 27px; color: var(--silver-soft);
  }
</style>
</head>
<body>
<main class="sheet">

  <section class="card card--front" aria-label="Business card front">
    <div class="brand">Qelmora Holdings Ltd.</div>

    <div class="holder">
      <div class="holder__name">Elias Marr</div>
      <div class="holder__role">Director</div>
    </div>

    <ul class="contact">
      <li class="contact__item">2240 Harbour Rd,
        <svg class="contact__icon" viewBox="0 0 24 24" aria-hidden="true"><path d="M12 3 2 12h3v9h5v-6h4v6h5v-9h3z"/></svg>
      </li>
      <li class="contact__item contact__item--continued">Kellworth Bay Singapore</li>
      <li class="contact__item">03 5550 1840
        <svg class="contact__icon" viewBox="0 0 24 24" aria-hidden="true"><path d="M2 9c0-3 4-5 10-5s10 2 10 5v2h-5V8H7v3H2zM6 12h12l3 8H3zm6 2a2.5 2.5 0 1 0 0 5 2.5 2.5 0 0 0 0-5z"/></svg>
      </li>
      <li class="contact__item">03 5550 1840
        <svg class="contact__icon" viewBox="0 0 24 24" aria-hidden="true"><path d="M6 2h9l3 3v5H6zM3 11h18v8h-3v3H6v-3H3zm5 5v4h8v-4z"/></svg>
      </li>
      <li class="contact__item">0400 555 172
        <svg class="contact__icon" viewBox="0 0 24 24" aria-hidden="true"><path d="M7 1h10a2 2 0 0 1 2 2v18a2 2 0 0 1-2 2H7a2 2 0 0 1-2-2V3a2 2 0 0 1 2-2zm0 3v14h10V4zm5 15.5a1.2 1.2 0 1 0 0 2.4 1.2 1.2 0 0 0 0-2.4z"/></svg>
      </li>
      <li class="contact__item">info@qelmora-example.com
        <svg class="contact__icon" viewBox="0 0 24 24" aria-hidden="true"><path d="M2 5h20v14H2zm2 2v.5l8 6 8-6V7l-8 6z"/></svg>
      </li>
    </ul>
  </section>

  <section class="card card--back" aria-label="Business card back">
    <div class="brand">Qelmora Holdings Ltd.</div>
    <div class="website">www.qelmora-example.com</div>
  </section>

</main>
</body>
</html>
```